Thank You For Shopping / Hair Care Tips

I need “Thank You For Shopping”
Post cards made for my hair business !
I added pictures of post cards that I really like . I also added my LunaVex Wigs logo for you guys to use

I want the backside of the flyer to have hair care tips !
I want people to have full directions on how to care for their wigs

Target Market(s)

Im marking to young woman to older middle aged woman
Ages 23-66 . I want my flyer to look mature And classy

Industry/Entity Type

Hair And Beauty

Font styles to use
Serif
Script

Colors
e34699
e34298
e34398

Requirements
Must have
• The flyer must have the Instagram logo with my Instagram name next to it @luna.vex.wigs__
• Also it must have my “Luna Vex Wigs” logo that I’ve uploaded in the pictures section .
• Flyer had to be two sides . One side “ thank you for shopping “ side two “hair care tips”
• My website must be on the flyer - www.lunavexwigs.example
• The flyer must match the colors of my logo
• All white . With the pink and glitter sliver you see on my logo
Nice to have
• Nice to have a glitter border
Should not have
• The flyer should not have different colors that don’t match my logo
• It shouldn’t be made without having my Instagram or website on the flyer

```html
<!DOCTYPE html>
<html lang="en">
<head>
<meta charset="utf-8">
<title>Hair Care Tips</title>
<link href="https://fonts.googleapis.com/css2?family=Pinyon+Script&family=Sorts+Mill+Goudy&display=swap" rel="stylesheet">
<style>
  :root {
    --paper: #ffffff;
    --card: #fbfbfb;
    --glitter-pink: #e34398;
    --glitter-deep: #8a1f5c;
    --title-pink: #e681bd;
    --text-pink: #e27bb8;
  }
  * { margin: 0; padding: 0; box-sizing: border-box; }
  html, body {
    width: 1200px;
    height: 927px;
    overflow: hidden;
    background: var(--paper);
  }
  .postcard {
    position: relative;
    width: 1200px;
    height: 927px;
    background: var(--paper);
  }
  .glitter-frame {
    position: absolute;
    left: 38px;
    top: 27px;
    width: 1124px;
    height: 872px;
    background: linear-gradient(135deg, var(--glitter-pink) 0%, var(--glitter-deep) 50%, var(--glitter-pink) 100%);
  }
  .card-face {
    position: absolute;
    left: 61px;
    top: 53px;
    width: 1078px;
    height: 823px;
    background: var(--card);
  }
  .tips-title {
    position: absolute;
    left: 0;
    top: 88px;
    width: 100%;
    text-align: center;
    font-family: "Pinyon Script", cursive;
    font-weight: 400;
    font-size: 104px;
    line-height: 1;
    color: var(--title-pink);
  }
  .tips-list {
    position: absolute;
    left: 134px;
    top: 286px;
    width: 920px;
    list-style: none;
    font-family: "Sorts Mill Goudy", serif;
    font-size: 23px;
    line-height: 27px;
    color: var(--text-pink);
  }
  .tips-list li { margin-bottom: 28px; }
</style>
</head>
<body>
  <main class="postcard">
    <div class="glitter-frame" role="img" aria-label="Pink glitter border"></div>
    <section class="card-face">
      <h1 class="tips-title">Hair Care Tips</h1>
    </section>
    <ul class="tips-list">
      <li>Wash or rinse all human hair products and style before wearing. Human hair is not ready to wear out of the box.</li>
      <li>Rinsing with hot water will damage the cap.</li>
      <li>Do not dry on a solid form or mannequin head to avoid stretching the cap.</li>
      <li>We do not recommend sleeping, showering or swimming while wearing the wig.</li>
      <li>Store the wig on a wig stand to avoid unwanted kinks or crimps.</li>
      <li>Lace is delicate and should not be tugged or pulled.</li>
      <li>Avoid brushing the hair when wet to prevent damage.</li>
      <li>Any cutting or chemical processes, such as perming or coloring, should be done by a professional hair stylist. We do not recommend lifting or bleaching human hair; depositing color provides the best result.</li>
    </ul>
  </main>
</body>
</html>
```